Flyer Design Dental Office Grand Opening offer

Dental office.

Grand opening flyer. Offer Exam + cleaning + xrays.
special: free teeth whitening ($200 value)

Target Market(s)

Middle class people around Huntington Beach.

Industry/Entity Type

Dental Clinic

Colors
cfeae6
86cfc6
fac994
fee18a
e667a6

Requirements
Must have
• Do not change my existing logo
Nice to have
• Have some appealing picture/design to catch the eye, but not too flashy
Should not have
• No cartoon kind of design

```html
<!DOCTYPE html>
<html lang="en">
<head>
<meta charset="utf-8">
<title>Harbor Light Dental – Grand Opening Special</title>
<link rel="stylesheet" href="https://fonts.googleapis.com/css2?family=Montserrat:wght@500;600;700&family=Nunito+Sans:wght@400;600&display=swap">
<style>
  :root {
    --mint: #cfeae6;
    --teal: #86cfc6;
    --teal-deep: #1fa9a4;
    --peach: #fac994;
    --butter: #fee18a;
    --pink: #e667a6;
    --ink: #5f6163;
    --ink-dark: #3a3a3a;
    --rule: #17a5a0;
    --paper: #ffffff;
  }
  * { box-sizing: border-box; margin: 0; padding: 0; }
  html, body { width: 941px; height: 1200px; overflow: hidden; background: var(--paper); }
  .flyer { position: relative; width: 941px; height: 1200px; background: var(--paper); font-family: "Nunito Sans", sans-serif; color: var(--ink-dark); }
  .abs { position: absolute; }

  .brand { right: 69px; top: 50px; display: flex; align-items: center; gap: 12px; }
  .brand-dot { width: 34px; height: 34px; border-radius: 50%; background: var(--teal-deep); }
  .brand-name { font-family: "Montserrat", sans-serif; font-weight: 600; font-size: 34px; color: var(--teal-deep); letter-spacing: 1px; }
  .doctor { right: 69px; top: 122px; font-family: Georgia, serif; font-size: 20px; font-weight: 700; color: var(--ink-dark); }

  .header-rule { left: 29px; top: 159px; width: 883px; height: 4px; background: var(--rule); }

  .hero-photo { left: 302px; top: 164px; width: 610px; height: 334px;
    background: linear-gradient(90deg, #ffffff 0%, #d9d9d9 14%, #8a8a8a 40%, #bdbdbd 70%, #dcdcdc 100%); }

  .headline { left: 69px; top: 248px; font-family: "Montserrat", sans-serif; font-weight: 600; font-size: 53px; line-height: 62px; color: var(--ink); letter-spacing: 1px; }
  .headline .accent { color: var(--peach); }

  .offer-panel { left: 29px; top: 501px; width: 883px; height: 564px; background: var(--mint); }
  .stripe-pink { left: 29px; top: 521px; width: 883px; height: 10px; background: var(--pink); }
  .stripe-butter { left: 173px; top: 531px; width: 739px; height: 17px; background: var(--butter); }

  .price { font-family: "Montserrat", sans-serif; font-weight: 700; font-size: 54px; }
  .price-pink { left: 186px; top: 608px; color: var(--pink); }
  .price-teal { left: 186px; top: 782px; color: var(--teal-deep); }

  .offer-title { font-size: 38px; line-height: 44px; color: var(--ink-dark); }
  .offer-sub { font-size: 26px; line-height: 32px; color: var(--ink-dark); }
  .offer-value { color: var(--teal-deep); }
  .exam { left: 347px; top: 620px; }
  .bleach { left: 347px; top: 792px; }

  .divider { left: 158px; width: 677px; border-top: 2px dashed var(--teal-deep); }
  .divider-one { top: 751px; }
  .divider-two { top: 886px; }

  .plans { left: 345px; top: 943px; font-family: "Montserrat", sans-serif; font-weight: 600; font-size: 26px; color: var(--ink); letter-spacing: 0.5px; }

  .contact-band { left: 29px; top: 1068px; width: 883px; height: 100px; background: var(--teal); }
  .call { left: 79px; top: 1100px; color: var(--paper); font-size: 40px; }
  .call strong { font-family: "Montserrat", sans-serif; font-weight: 700; margin-right: 14px; }
  .call .phone { font-family: "Nunito Sans", sans-serif; font-weight: 400; }
  .address { right: 86px; top: 1094px; text-align: right; font-size: 20px; line-height: 26px; color: var(--ink-dark); }
</style>
</head>
<body>
<main class="flyer">
  <div class="abs brand"><span class="brand-dot"></span><span class="brand-name">Harbor Light Dental</span></div>
  <div class="abs doctor">Linh Tran, DDS</div>
  <div class="abs header-rule"></div>

  <div class="abs hero-photo" role="img" aria-label="Black and white close-up photograph of a smiling woman's lips and long hair"></div>

  <h1 class="abs headline">GRAND<br>OPENING<br><span class="accent">SPECIAL</span></h1>

  <div class="abs offer-panel"></div>
  <div class="abs stripe-pink"></div>
  <div class="abs stripe-butter"></div>

  <div class="abs price price-pink">$50</div>
  <div class="abs exam">
    <p class="offer-title">Exam</p>
    <p class="offer-sub">with Xrays &amp; Cleaning (regular)</p>
    <p class="offer-sub offer-value">value of $200</p>
  </div>
  <div class="abs divider divider-one"></div>

  <div class="abs price price-teal">Free</div>
  <div class="abs bleach">
    <p class="offer-title">Bleaching</p>
    <p class="offer-sub">(after completion of dental treatment)</p>
  </div>
  <div class="abs divider divider-two"></div>

  <p class="abs plans">PPO, HMO, STATE PLANS WELCOMED</p>

  <div class="abs contact-band"></div>
  <p class="abs call"><strong>CALL</strong><span class="phone">(714) 555 - 0182</span></p>
  <address class="abs address" style="font-style:normal">4127 Seacliff Ave<br>Huntington Beach, CA 92649</address>
</main>
</body>
</html>
```